Business card, Letterhead and envelope design
Create a business card, letterhead and envelope design for Velmira Solutions
Professional
name
title
address
email@velmira-example.com
www.velmirasolutions-example.com
logo and font
Trifold brochure design we have for inspiration of design. This is for reference only.

```html
<!DOCTYPE html>
<html lang="en">
<head>
<meta charset="utf-8">
<title>Velmira Solutions Stationery</title>
<link rel="stylesheet" href="https://fonts.googleapis.com/css2?family=Open+Sans:wght@400;600;700&display=swap">
<style>
:root{
  --backdrop:#a8a8aa;
  --paper:#ffffff;
  --brand-blue:#3b8fd8;
  --brand-blue-light:#6fb2ea;
  --brand-navy:#1f3f6e;
  --text-grey:#555a61;
  --pattern-tint:#e6eef6;
  --card-tint:#b9d3ea;
}
*{margin:0;padding:0;box-sizing:border-box}
html,body{width:1200px;height:684px;overflow:hidden}
body{background:var(--backdrop);font-family:"Open Sans",sans-serif;position:relative}
.sheet{position:absolute;background:var(--paper);box-shadow:0 1px 3px rgba(0,0,0,.25);overflow:hidden}
.band{position:absolute;left:0;right:0;background:linear-gradient(var(--brand-blue-light),var(--brand-blue))}
.band-top{top:0}
.band-bottom{bottom:0;display:flex;align-items:center;padding-left:14px}
.band-url{color:#fff;font-size:6px}
.pattern{position:absolute;background:linear-gradient(135deg,rgba(230,238,246,0) 0%,var(--pattern-tint) 45%,rgba(230,238,246,.4) 100%)}
.brand{position:absolute;display:flex;align-items:center;gap:6px}
.brand-mark{background:var(--brand-navy)}
.brand-name{color:var(--brand-navy);font-weight:700;line-height:1.05}
.contact-line{position:absolute;font-size:5.5px;color:var(--text-grey);white-space:nowrap}

/* letterhead */
.letterhead{left:204px;top:19px;width:456px;height:641px}
.letterhead .band-top{height:17px}
.letterhead .band-bottom{height:17px}
.letterhead .pattern{left:0;top:17px;right:0;height:560px}
.letterhead .brand{left:18px;top:40px}
.letterhead .brand-mark{width:30px;height:30px}
.letterhead .brand-name{font-size:13px;width:70px}
.letterhead .contact-line{left:14px;bottom:26px}

/* business card */
.business-card{left:24px;top:283px;width:173px;height:96px;background:linear-gradient(135deg,var(--card-tint),#e7f0f8 60%,var(--card-tint))}
.business-card .brand{left:8px;top:12px;gap:4px}
.business-card .brand-mark{width:14px;height:14px}
.business-card .brand-name{font-size:8px;width:50px}
.card-person{position:absolute;right:6px;top:10px;text-align:right;color:var(--brand-navy)}
.card-name{font-size:6px;font-weight:600}
.card-title{font-size:5px}
.card-contacts{position:absolute;left:8px;top:52px;font-size:4.5px;color:var(--brand-navy);line-height:1.5}

/* envelope */
.envelope{left:696px;top:96px;width:480px;height:240px}
.envelope-flap{position:absolute;inset:0}
.envelope .brand{left:225px;top:12px}
.envelope .brand-mark{width:30px;height:30px}

/* compliment slip */
.slip{left:648px;top:372px;width:533px;height:242px}
.slip .band-top{height:14px}
.slip .band-bottom{height:14px}
.slip .pattern{left:0;top:14px;right:0;height:190px}
.slip .brand{left:14px;top:44px}
.slip .brand-mark{width:34px;height:34px}
.slip .brand-name{font-size:14px;width:74px}
.slip .contact-line{left:14px;bottom:22px}
</style>
</head>
<body>

<section class="sheet letterhead">
  <div class="band band-top"></div>
  <div class="pattern" role="img" aria-label="Faint light-blue stacked cube backdrop"></div>
  <div class="brand"><span class="brand-mark"></span><span class="brand-name">Velmira Solutions</span></div>
  <p class="contact-line">email@velmira-example.com | P: 212 555 0148 | F: 212 555 0149 | 18 Suite 4, Kent Park Road, NY 10018</p>
  <div class="band band-bottom"><span class="band-url">www.velmirasolutions-example.com</span></div>
</section>

<section class="sheet business-card" role="img" aria-label="Business card with light-blue cube backdrop">
  <div class="brand"><span class="brand-mark"></span><span class="brand-name">Velmira Solutions</span></div>
  <div class="card-person">
    <p class="card-name">Aaron Pell</p>
    <p class="card-title">Managing Director</p>
  </div>
  <div class="card-contacts">
    <p>email@velmira-example.com</p>
    <p>P: 212 555 0148</p>
    <p>18 Kent Park Road, NY</p>
    <p>www.velmirasolutions-example.com</p>
  </div>
</section>

<section class="sheet envelope">
  <svg class="envelope-flap" viewBox="0 0 480 240" aria-hidden="true">
    <path d="M2 4 L210 112 Q240 126 270 112 L478 4" fill="none" stroke="#c9cdd2" stroke-width="1.2"/>
  </svg>
  <div class="brand"><span class="brand-mark"></span></div>
</section>

<section class="sheet slip">
  <div class="band band-top"></div>
  <div class="pattern" role="img" aria-label="Faint light-blue stacked cube backdrop"></div>
  <div class="brand"><span class="brand-mark"></span><span class="brand-name">Velmira Solutions</span></div>
  <p class="contact-line">email@velmira-example.com | P: 212 555 0148 | F: 212 555 0149 | 18 Suite 4, Kent Park Road, NY 10018</p>
  <div class="band band-bottom"><span class="band-url">www.velmirasolutions-example.com</span></div>
</section>

</body>
</html>
```